Editorial Website Design for High-End Custom Millwork Firm

Design (no development) for a 5-7 page website for a high-end custom architectural millwork firm. Editorial, magazine-quality aesthetic — think Dwelling Quarterly and top-tier millwork studios (Owen Tallard, Vorko). Full brief, reference sites, and project photography attached. We have uploaded a sample of our photography to use in your design. PLEASE READ PDF DOCUMENT BRIEF!!!

```html
<!DOCTYPE html>
<html lang="en">
<head>
<meta charset="utf-8">
<title>KDM — Architectural Millwork</title>
<link rel="stylesheet" href="https://fonts.googleapis.com/css2?family=Libre+Caslon+Text:wght@400&family=Montserrat:wght@400;500&display=swap">
<style>
:root{
  --ink:#1f1d1b;
  --cream:#ebe7e1;
  --cream-light:#eeebe6;
  --paper:#f5f2ee;
  --muted:#5e5852;
  --line:#8d867e;
  --dark:#1e1e1e;
  --dark-line:#4a4642;
  --dark-text:#cfc9c1;
}
*{box-sizing:border-box;margin:0;padding:0}
html,body{width:1200px;height:2700px;overflow:hidden}
body{position:relative;background:var(--cream);color:var(--ink);font-family:"Montserrat",sans-serif}
.serif{font-family:"Libre Caslon Text",serif;font-weight:400}
.abs{position:absolute}
.eyebrow{font-size:9px;letter-spacing:2px;text-transform:uppercase;font-weight:500}
.link{display:flex;justify-content:space-between;align-items:center;font-size:9.5px;letter-spacing:1.6px;text-transform:uppercase;font-weight:500;padding-bottom:12px;border-bottom:1px solid var(--line)}
.link svg{width:12px;height:8px}
.photo{position:absolute}

/* hero */
.hero{position:absolute;left:0;top:0;width:1200px;height:603px;background:linear-gradient(100deg,#2a1f18 0%,#4a3426 35%,#5b4130 60%,#3a2a20 85%,#2b2019 100%)}
.hero-shade{position:absolute;inset:0;background:linear-gradient(90deg,rgba(20,14,10,.55) 0%,rgba(20,14,10,.1) 55%,rgba(20,14,10,.25) 100%)}
.logo{position:absolute;left:26px;top:16px;font-size:56px;color:#f3efe9;letter-spacing:-1px}
.nav{position:absolute;right:48px;top:40px;display:flex;gap:38px;font-size:9.5px;letter-spacing:1.4px;color:#f1ece5;font-weight:500}
.hero h1{position:absolute;left:59px;top:228px;font-size:60px;line-height:62px;color:#f2ede6}
.hero .sub{position:absolute;left:59px;top:437px;font-size:10.5px;letter-spacing:1.2px;line-height:18px;color:#f1ece5;font-weight:500}
.hero .link{position:absolute;left:59px;top:503px;width:138px;color:#f1ece5;border-color:rgba(241,236,229,.5)}

/* about */
.about{position:absolute;left:0;top:603px;width:1200px;height:356px;background:var(--cream-light)}
.about .eyebrow{position:absolute;left:154px;top:80px}
.about p{position:absolute;left:154px;top:112px;width:370px;font-size:20px;line-height:28px}
.about .link{position:absolute;left:154px;top:256px;width:112px}

/* services */
.services{position:absolute;left:0;top:959px;width:1200px;height:314px;background:var(--dark);color:#efeae3}
.services .eyebrow{position:absolute;left:154px;top:42px;color:#cfc9c1}
.services h2{position:absolute;left:154px;top:66px;font-size:31px}
.services .link{position:absolute;left:892px;top:92px;width:154px;color:#efeae3;border-color:var(--dark-line)}
.step{position:absolute;top:138px;width:200px;height:120px}
.step .num{font-family:"Libre Caslon Text",serif;font-size:17px}
.step h3{font-size:10px;letter-spacing:1.6px;font-weight:500;margin-top:13px}
.step p{font-size:11.5px;line-height:20px;color:var(--dark-text);margin-top:15px}
.divider{position:absolute;top:139px;width:1px;height:118px;background:var(--dark-line)}

/* featured */
.featured{position:absolute;left:0;top:1273px;width:1200px;height:584px;background:var(--cream)}
.featured .eyebrow{position:absolute;left:154px;top:41px}
.featured h2{position:absolute;left:154px;top:68px;font-size:31px;line-height:36px}
.featured .link{position:absolute;left:889px;top:118px;width:151px}
.card{position:absolute;top:178px;width:261px}
.card .photo{position:relative;height:320px}
.card .eyebrow{position:static;font-size:8.5px;margin-top:22px;color:var(--muted)}
.card .place{font-size:13px;margin-top:8px;color:#3d3832}

/* commitment */
.commit{position:absolute;left:0;top:1857px;width:1200px;height:307px;background:var(--cream-light)}
.commit .eyebrow{position:absolute;left:697px;top:57px;font-size:8.5px}
.commit h2{position:absolute;left:697px;top:82px;font-size:29px}
.commit p{position:absolute;left:697px;top:134px;width:290px;font-size:12.5px;line-height:19px;color:#3d3832}
.commit .link{position:absolute;left:697px;top:250px;width:130px}

/* journal */
.journal{position:absolute;left:0;top:2164px;width:1200px;height:390px;background:var(--cream)}
.journal .eyebrow{position:absolute;left:154px;top:37px;font-size:8.5px}
.journal h2{position:absolute;left:154px;top:60px;font-size:29px;line-height:32px}
.journal .link{position:absolute;left:887px;top:100px;width:150px}
.post{position:absolute;top:148px}
.post .photo{position:relative;height:149px}
.post .kicker{font-family:"Libre Caslon Text",serif;font-size:11.5px;color:var(--muted);margin-top:20px}
.post .title{font-family:"Libre Caslon Text",serif;font-size:13.5px;margin-top:3px}
.post .date{font-size:7.5px;letter-spacing:1px;margin-top:12px;color:var(--muted)}

/* footer */
.footer{position:absolute;left:0;top:2554px;width:1200px;height:146px;background:var(--dark);color:#ece6de}
.footer .brand{position:absolute;left:154px;top:14px;font-size:33px}
.footer .tag{position:absolute;left:154px;top:66px;font-size:8.5px;letter-spacing:1.2px;line-height:15px;font-weight:500}
.footer .social{position:absolute;left:154px;top:110px;display:flex;gap:12px}
.footer .social span{width:13px;height:13px;border:1.4px solid #ece6de;border-radius:50%}
.fcol{position:absolute;top:45px;font-size:8.5px;letter-spacing:1.2px;line-height:24px;font-weight:500}
.contact{position:absolute;right:153px;top:45px;text-align:right;font-size:8.5px;letter-spacing:1.1px;line-height:20px;font-weight:500}
.copy{position:absolute;right:153px;top:115px;font-size:8px;letter-spacing:1px;color:#bdb6ad}
</style>
</head>
<body>

<header class="hero">
  <div class="photo" role="img" aria-label="Dark walnut-panelled entry hall with a curved staircase, a round fluted pedestal table and a black vase holding olive branches" style="inset:0;background:linear-gradient(95deg,#2c2119 0%,#3f2d22 28%,#5a4131 52%,#4b3527 72%,#2e221a 100%)"></div>
  <div class="hero-shade"></div>
  <div class="logo serif">KDM</div>
  <nav class="nav"><span>ABOUT</span><span>SERVICES</span><span>PORTFOLIO</span><span>PROCESS</span><span>JOURNAL</span><span>CONTACT</span></nav>
  <h1 class="serif">Architectural<br>Millwork.<br>Reimagined.</h1>
  <div class="sub">BESPOKE MILLWORK AND INTERIORS<br>CRAFTED WITH PRECISION. BUILT TO LAST.</div>
  <div class="link"><span>View our work</span><svg viewBox="0 0 12 8"><path d="M0 4h11M8 1l3 3-3 3" fill="none" stroke="currentColor"/></svg></div>
</header>

<section class="about">
  <div class="eyebrow">KDM</div>
  <p class="serif">We partner with architects, designers, and builders to create exceptional millwork and interiors that elevate spaces and stand the test of time.</p>
  <div class="link"><span>About KDM</span><svg viewBox="0 0 12 8"><path d="M0 4h11M8 1l3 3-3 3" fill="none" stroke="currentColor"/></svg></div>
  <div class="photo" role="img" aria-label="Walnut kitchen with marble backsplash, island with stools and black pendant lights" style="left:633px;top:47px;width:496px;height:271px;background:linear-gradient(180deg,#cfc8bd 0%,#8a7563 30%,#5b4333 65%,#3a2b21 100%)"></div>
</section>

<section class="services">
  <div class="eyebrow">Services</div>
  <h2 class="serif">From concept to completion.</h2>
  <div class="link"><span>Explore our process</span><svg viewBox="0 0 12 8"><path d="M0 4h11M8 1l3 3-3 3" fill="none" stroke="currentColor"/></svg></div>
  <div class="step" style="left:154px"><div class="num">01</div><h3>CONSULTATION</h3><p>Collaborative planning<br>and detailing to bring<br>your vision to life.</p></div>
  <div class="divider" style="left:343px"></div>
  <div class="step" style="left:387px"><div class="num">02</div><h3>DESIGN DEVELOPMENT</h3><p>Technical expertise and<br>detail-driven solutions<br>for every project.</p></div>
  <div class="divider" style="left:578px"></div>
  <div class="step" style="left:623px"><div class="num">03</div><h3>CRAFTSMANSHIP</h3><p>Precision fabrication using<br>the finest materials and<br>proven techniques.</p></div>
  <div class="divider" style="left:814px"></div>
  <div class="step" style="left:858px"><div class="num">04</div><h3>INSTALLATION</h3><p>Seamless execution and<br>flawless installation<br>on time, every time.</p></div>
</section>

<section class="featured">
  <div class="eyebrow">Featured work</div>
  <h2 class="serif">Thoughtfully designed.<br>Meticulously crafted.</h2>
  <div class="link"><span>View full portfolio</span><svg viewBox="0 0 12 8"><path d="M0 4h11M8 1l3 3-3 3" fill="none" stroke="currentColor"/></svg></div>
  <div class="card" style="left:46px"><div class="photo" role="img" aria-label="Walnut kitchen with marble backsplash and island stools" style="background:linear-gradient(180deg,#5b4434 0%,#9d8d7c 45%,#6b4f3b 75%,#3d2d22 100%)"></div><div class="eyebrow">Private residence</div><div class="place">Austin, Texas</div></div>
  <div class="card" style="left:329px"><div class="photo" role="img" aria-label="Walk-in closet lined with walnut shelving and drawers" style="background:linear-gradient(180deg,#3f2e22 0%,#5c4332 50%,#8a6e55 85%,#a88d70 100%)"></div><div class="eyebrow">Private residence</div><div class="place">Dallas, Texas</div></div>
  <div class="card" style="left:611px"><div class="photo" role="img" aria-label="Bathroom vanity with fluted walnut front and marble top" style="background:linear-gradient(180deg,#d9d4cc 0%,#c5bdb2 42%,#7a5b43 60%,#5d4331 90%,#4a3628 100%)"></div><div class="eyebrow">Private residence</div><div class="place">Miami, Florida</div></div>
  <div class="card" style="left:893px"><div class="photo" role="img" aria-label="Living room with walnut built-in shelving around a fireplace and white sofas" style="background:linear-gradient(180deg,#6a4e3a 0%,#5a4131 50%,#b2a79a 80%,#cfc7bc 100%)"></div><div class="eyebrow">Private residence</div><div class="place">Nashville, Tennessee</div></div>
</section>

<section class="commit">
  <div class="photo" role="img" aria-label="Close-up of a walnut cabinet corner showing dovetail joinery" style="left:0;top:0;width:588px;height:307px;background:linear-gradient(120deg,#2a1a12 0%,#5e3a26 40%,#7a4c32 60%,#3a2418 100%)"></div>
  <div class="eyebrow">Our commitment</div>
  <h2 class="serif">Quality in every detail.</h2>
  <p>We believe exceptional spaces begin with exceptional craftsmanship. Every piece we create is a reflection of our commitment to quality, precision, and enduring beauty.</p>
  <div class="link"><span>Our approach</span><svg viewBox="0 0 12 8"><path d="M0 4h11M8 1l3 3-3 3" fill="none" stroke="currentColor"/></svg></div>
</section>

<section class="journal">
  <div class="eyebrow">Journal</div>
  <h2 class="serif">Insights on design,<br>craftsmanship, and process.</h2>
  <div class="link"><span>Read the journal</span><svg viewBox="0 0 12 8"><path d="M0 4h11M8 1l3 3-3 3" fill="none" stroke="currentColor"/></svg></div>
  <article class="post" style="left:154px;width:284px"><div class="photo" role="img" aria-label="Tall walnut cabinet doors in soft light" style="background:linear-gradient(90deg,#4a3323 0%,#8a6446 40%,#a07a58 60%,#4a3324 100%)"></div><div class="kicker">The Beauty of Bespoke</div><div class="title">Why Custom Millwork Matters</div><div class="date">MAY 12, 2024</div></article>
  <article class="post" style="left:465px;width:268px"><div class="photo" role="img" aria-label="Stacked wood and stone material samples" style="background:linear-gradient(160deg,#9e958b 0%,#b8afa3 35%,#6d5644 65%,#2c2620 100%)"></div><div class="kicker">Materiality and Detail</div><div class="title">Creating Timeless Interiors</div><div class="date">APRIL 28, 2024</div></article>
  <article class="post" style="left:761px;width:285px"><div class="photo" role="img" aria-label="Millwork workshop with benches and cabinetry in progress" style="background:linear-gradient(180deg,#6e5138 0%,#a07c5a 45%,#7b5c42 75%,#4a3526 100%)"></div><div class="kicker">Behind the Build</div><div class="title">A Look Inside Our Process</div><div class="date">APRIL 10, 2024</div></article>
</section>

<footer class="footer">
  <div class="brand serif">KDM</div>
  <div class="tag">ARCHITECTURAL MILLWORK<br>AND INTERIORS</div>
  <div class="social" aria-label="Social links"><span></span><span></span></div>
  <div class="fcol" style="left:465px">ABOUT<br>SERVICES<br>PORTFOLIO</div>
  <div class="fcol" style="left:613px">PROCESS<br>JOURNAL<br>CONTACT</div>
  <div class="contact">INFO@KDMMILLWORK.COM<br>512.555.0143<br>AUSTIN, TEXAS</div>
  <div class="copy">© KDM MILLWORK, LLC. ALL RIGHTS RESERVED.</div>
</footer>

</body>
</html>
```